New high end server provider needs wordpress design

www.kv7hostrack.com

Need a wordpress design for a high end server provider that provides overclocked dedicated servers for rent. We are located in Chicago but we have a presence is Virginia and Nevada for both our east and west coast customers.

We are a server provider that specializes in top end hardware with every feature designed for optimum performance. If it is not the best quality part or provides the best possible performance we don't run it. Our customers are mainly those that want the best single threaded performance possible from their hardware. We would be selling our services directly on our website via WHMCS.

We would like to see designs that are very modern and simplistic yet very attractive looking and catchy. Would prefer colors in the blues and greens and white. These colors are not necessary and I would be open to another color scheme if it looks good.

The final design should show speed and performance while being simplistic and easy on the eyes.
Updates

Logo and company name added and payment changed to guaranteed.  Looking for a wordpress template with the same pages as kv7hostrack.com but with a redesigned look and feel.  

WHMCS control panel design also part of the design request.

If you have any questions please let me know!  This is just for kv7hostrack.com and a main page for WHMCS (no coding just design).

Target Market(s)

IT Guru's (mostly men in their 20's to 30's)

Industry/Entity Type

Hardware

Requirements
Must have
• WHMCS panel design to fit with website theme.
Nice to have
• Main slider on home page similar to one of our other websites at www.kv7hostrack.com
Should not have
• Flash or frames

```html
<!DOCTYPE html>
<html lang="en">
<head>
<meta charset="utf-8">
<title>KV7HOSTRACK – Dedicated Servers</title>
<link href="https://fonts.googleapis.com/css2?family=Oswald:wght@400;500;600&family=Open+Sans:wght@400;600;700&display=swap" rel="stylesheet">
<style>
:root{
  --navy:#0b2a44;
  --deep:#06182a;
  --hero-a:#0d3a5c;
  --hero-b:#1f6f9c;
  --teal-a:#4fd6ea;
  --teal-b:#1796b8;
  --orange-a:#ffa43a;
  --orange-b:#ee5f06;
  --green-a:#a8e04a;
  --green-b:#54a914;
  --ink:#333;
  --muted:#555;
  --line:#dcdcdc;
  --panel:#efefef;
  --white:#fff;
  --footer-text:#d6e3ee;
  --footer-dim:#a9bfd2;
}
*{margin:0;padding:0;box-sizing:border-box}
html,body{width:779px;height:1200px;overflow:hidden;background:var(--white)}
body{position:relative;font-family:"Open Sans",sans-serif;color:var(--ink)}
.abs{position:absolute}

/* header */
.site-header{left:0;top:0;width:779px;height:55px;background:var(--white);box-shadow:0 1px 3px rgba(0,0,0,.15);z-index:2}
.brand{left:76px;top:15px;width:145px;height:28px;background:var(--deep);border-radius:14px;color:var(--white);font:600 17px/28px "Oswald",sans-serif;letter-spacing:.5px;text-align:center}
.main-nav{left:258px;top:0;height:55px;display:flex}
.main-nav a{font:400 9.5px/55px "Open Sans",sans-serif;color:#333;text-decoration:none;padding:0 8px;text-transform:uppercase;white-space:nowrap}

/* hero */
.hero{left:0;top:55px;width:779px;height:156px;background:radial-gradient(ellipse at 40% 40%,var(--hero-b),var(--hero-a) 60%,var(--deep))}
.hero-art{left:427px;top:0;width:240px;height:156px;background:linear-gradient(180deg,#9aa6ae,#4e5a62 70%,#2c3840)}
.hero-title{left:74px;top:68px;color:var(--white);font:500 35px/1 "Oswald",sans-serif}
.hero-sub{left:75px;top:110px;color:var(--white);font:700 14px/1 "Open Sans",sans-serif}
.hero-sub span{font-weight:400}

/* choose */
.choose{left:176px;top:240px;width:427px;height:78px;border:2px solid #cfcfcf;border-radius:4px;background:linear-gradient(#fafafa,#e6e6e6);text-align:center}
.choose h1{font:600 32px/1 "Oswald",sans-serif;color:#2a8fb0;margin-top:10px}
.choose p{font:400 12.5px/1 "Oswald",sans-serif;color:#999;margin-top:6px;letter-spacing:.3px}
.intro{left:80px;top:333px;width:619px;text-align:center;font-size:10px;line-height:13px;color:var(--muted)}

/* pricing */
.plan{background:var(--white);border:1px solid var(--line);border-radius:8px;box-shadow:0 2px 6px rgba(0,0,0,.12);text-align:center}
.plan-basic{left:76px;top:410px;width:196px;height:350px}
.plan-plus{left:277px;top:395px;width:223px;height:385px;box-shadow:0 3px 10px rgba(0,0,0,.25)}
.plan-custom{left:504px;top:410px;width:198px;height:350px}
.plan-head{margin:7px auto 0;border-radius:5px;padding-top:6px;height:52px}
.plan-head.teal{width:186px;background:linear-gradient(var(--teal-a),var(--teal-b));color:#0b3346}
.plan-head.orange{width:205px;background:linear-gradient(var(--orange-a),var(--orange-b));color:#5a1f00;height:54px}
.plan-head b{display:block;font:600 22px/1 "Oswald",sans-serif}
.plan-head small{display:block;font:500 12px/1.2 "Oswald",sans-serif;text-transform:uppercase}
.price{font:600 38px/1 "Oswald",sans-serif;color:#333;margin:20px 0 18px}
.price sup{font-size:18px;vertical-align:14px}
.price em{font-style:normal;font-size:15px;font-weight:400}
.features{list-style:none;margin:0 14px}
.features li{font-size:9px;line-height:22.5px;border-bottom:1px solid var(--line);color:#444;white-space:nowrap}
.features li:last-child{border:0}
.btn{border-radius:5px;font:400 17px/36px "Oswald",sans-serif;color:#13405a;text-align:center;text-transform:uppercase}
.btn.teal{background:linear-gradient(var(--teal-a),var(--teal-b))}
.btn.orange{background:linear-gradient(var(--orange-a),var(--orange-b));color:#6a2400}
.btn-basic{left:121px;top:747px;width:112px;height:36px}
.btn-plus{left:328px;top:762px;width:120px;height:36px}
.btn-custom{left:546px;top:747px;width:112px;height:36px}

/* quote */
.quote{left:93px;top:836px;width:587px;height:106px;background:var(--panel);border:1px solid #d4d4d4;border-radius:12px;text-align:center}
.quote p{font-size:12.5px;color:#222;margin-top:18px}
.quote-btn{left:183px;top:44px;width:225px;height:40px;border-radius:20px;background:linear-gradient(var(--green-a),var(--green-b));border:2px solid #d9f2b5;color:var(--white);font:500 14px/36px "Oswald",sans-serif;text-align:left;padding-left:16px}
.quote-btn svg{position:absolute;right:6px;top:5px}
.partners{left:244px;top:957px;display:flex;gap:48px;align-items:center}
.partner-badge{width:78px;height:18px;background:#222;border-radius:2px}
.partner-badge.round{width:40px;height:24px;border-radius:50%;background:none;border:2px solid #555}

/* footer */
.site-footer{left:0;top:998px;width:779px;height:202px;background:linear-gradient(160deg,#12466a,#0b2e4a 55%,#082238)}
.footer-mark{left:120px;top:18px;width:64px;height:56px;border-radius:50%;background:#123a58}
.footer-brand{left:92px;top:84px;font:600 24px/1 "Oswald",sans-serif;color:#123a58}
.footer-col{top:34px;font-size:8px;line-height:15px;color:var(--footer-dim);text-transform:uppercase}
.footer-col h3{font:700 10.5px/18px "Open Sans",sans-serif;color:var(--white)}
.connect{left:178px;top:144px;font-size:9.5px;color:var(--white);letter-spacing:.5px;display:flex;align-items:center;gap:11px}
.dot{width:9px;height:9px;border-radius:50%;background:var(--white)}
.subscribe{left:414px;top:140px;width:182px;height:17px;background:#0e3d60;border:1px solid #1c5378;font-size:8px;line-height:15px;color:#4d7a99;padding-left:6px}
.subscribe span{position:absolute;right:6px;color:#cfe0ec}
.copyright{left:0;top:185px;width:779px;text-align:center;font-size:8px;color:#3f7097}
</style>
</head>
<body>

<header class="site-header abs">
  <div class="brand abs">KV7HOSTRACK</div>
  <nav class="main-nav abs">
    <a>Our Servers</a><a>Dedicated Servers</a><a>Why KV7?</a><a>Testimonials</a><a>FAQ's</a><a>Contacts</a>
  </nav>
</header>

<section class="hero abs">
  <div class="hero-art abs" role="img" aria-label="Row of rack-mounted servers with a laptop in front"></div>
  <h2 class="hero-title abs">Dedicated Servers</h2>
  <p class="hero-sub abs">Dual Vextra Quad Core <span>with</span> 16GB RAM + 1TB Storage.</p>
</section>

<div class="choose abs">
  <h1>CHOOSE A DEDICATED SERVER</h1>
  <p>QUICK AND ESY SETUP . GREAT PRICE! &nbsp;BUILT FOR RAW SPEED...</p>
</div>
<p class="intro abs">It is a long established fact that a reader will be distracted by the readable content of a page when looking at its layout. The point of using Lorem Ipsum is that it has a more-or-less normal distribution of letters, as opposed to using 'Content here, content here', making it look like readable English...</p>

<article class="plan plan-basic abs">
  <div class="plan-head teal"><b>BASIC</b><small>Community Package</small></div>
  <div class="price"><sup>$</sup> 160/<em> MO.</em></div>
  <ul class="features">
    <li>Vextra Q-Series 4.4 Ghz CPU</li><li>8 GB DDR3 1600 Ram</li><li>320 GB Hard Drive</li><li>4 IP addresses</li>
    <li>1,500 GB monthly Bandwidth</li><li>(3) KV7 servers pre-configured</li><li>(1) Website hosting</li><li>Remote Desktop Access</li>
  </ul>
</article>
<article class="plan plan-plus abs">
  <div class="plan-head orange"><b>COMMUNITY</b><small>Package Plus</small></div>
  <div class="price"><sup>$</sup> 185/<em> MO.</em></div>
  <ul class="features">
    <li>Vextra Q-Series 4.4 Ghz CPU</li><li>8 GB DDR3 1600 Ram</li><li>320 GB Hard Drive</li><li>4 IP addresses</li>
    <li>1,500 GB monthly Bandwidth</li><li>(3) KV7 servers pre-configured</li><li>(1) Website hosting</li><li>Remote Desktop Access</li>
  </ul>
</article>
<article class="plan plan-custom abs">
  <div class="plan-head teal"><b>CUSTOM</b><small>Community Package</small></div>
  <div class="price">VARIES/<em> MO.</em></div>
  <ul class="features">
    <li>Up to Vextra Q-Series 4.5 Ghz CPU</li><li>Up to 16 GB DDR3 1600 RAM</li><li>up to 1 TB Hard Drive</li><li>up to 5 IP Addresses</li>
    <li>up to 3,000 GB Monthly Bandwidth</li><li>(3) KV7 servers pre-configured</li><li>up to (2) Website hosting</li><li>Remote Desktop Access</li>
  </ul>
</article>
<div class="btn teal btn-basic abs">Sign Up</div>
<div class="btn orange btn-plus abs">Sign Up</div>
<div class="btn teal btn-custom abs">Sign Up</div>

<section class="quote abs">
  <p>Need a bigger plan? Contact us for a custom quote. We will get back to you within 24 hours.</p>
  <div class="quote-btn abs">REQUEST CUSTOM QUOTE
    <svg width="26" height="26" viewBox="0 0 26 26"><circle cx="13" cy="13" r="12" fill="#fff"/><path d="M7 11h7V7l6 6-6 6v-4H7z" fill="#3f8f10"/></svg>
  </div>
</section>
<div class="partners abs">
  <div class="partner-badge"></div>
  <div class="partner-badge round"></div>
  <div class="partner-badge"></div>
</div>

<footer class="site-footer abs">
  <div class="footer-mark abs"></div>
  <div class="footer-brand abs">KV7HOSTRACK</div>
  <div class="footer-col abs" style="left:319px"><h3>ABOUT</h3>Locations<br>Team<br>Careers</div>
  <div class="footer-col abs" style="left:395px"><h3>WORK</h3>Portfolio<br>Services</div>
  <div class="footer-col abs" style="left:471px"><h3>BLOGS</h3>Advance<br>Inspire<br>Extend<br>Flourish</div>
  <div class="footer-col abs" style="left:550px"><h3>MORE</h3>Idle Works<br>TalkScore<br>Team Norvale</div>
  <div class="footer-col abs" style="left:650px"><h3>CONTACT</h3>Send a message<br>Find us</div>
  <div class="connect abs">CONNECT WITH US : <i class="dot"></i><i class="dot"></i><i class="dot"></i><i class="dot"></i></div>
  <div class="subscribe abs">GET E-MAIL UPDATES<span>&rarr;</span></div>
  <p class="copyright abs">Copyright ©2013 KV7 Hostrack. All Right Reserved.</p>
</footer>

</body>
</html>
```